Cryptocurrency Advisor Business Card

Velbridge Consulting Services is my company, which advises many projects in the ICO/Cryptocurrency industry. I'd like to get a sleek, preferably matte black or matte dark blue finish, business card with the company name (and simple logo w/ crypto feel) on one side and while the other side I'd like a small twitter and telegram logo together maybe separated by a / as it's the same, then an email and a phone logo so I can insert those specifics there (no address). Can have name then CEO section too. At the bottom of that section, find a place for more of a job description: ICO Advisor, World Champion Gamer, Esports Award Winner, Varlomark Expert. You can possibly design a simple logo or use something with a crypto twist or background, but nothing too complex. Rounded edges for printing not square.
Updates

Had personal issues taking a few days away from me being able to provide feedback and check designs, etc. Will be more active now finalizing design just needed few days from issue but all is sorted.

Target Market(s)

Cryptocurrency industry

Industry/Entity Type

Management Consulting

Contact Information for Business Card

Font styles to use
Sans Serif

Colors
5c5c5c
474747
757575
9d9d9d
aaaaaa
333333
0355a3

Requirements
Must have
• Refer to Details/Description
Nice to have
Should not have
• Address section

```html
<!DOCTYPE html>
<html lang="en">
<head>
<meta charset="utf-8">
<title>Velbridge Consulting Services – Business Card</title>
<link rel="stylesheet" href="https://fonts.googleapis.com/css2?family=Montserrat:wght@300;400;700&display=swap">
<style>
  :root {
    --stage: #e4e4e4;
    --card-dark: #333333;
    --card-dark-2: #474747;
    --brand-blue: #0355a3;
    --brand-blue-deep: #02407c;
    --text-light: #ffffff;
    --text-muted: #aaaaaa;
    --icon-grey: #9d9d9d;
    --logo-grey: #757575;
  }
  * { box-sizing: border-box; margin: 0; padding: 0; }
  html, body { width: 1200px; height: 797px; overflow: hidden; }
  body {
    background: var(--stage);
    font-family: "Montserrat", Arial, sans-serif;
    display: flex;
    align-items: center;
    justify-content: center;
    gap: 40px;
  }
  .card {
    width: 540px;
    height: 309px;
    border-radius: 22px;
    overflow: hidden;
    position: relative;
    box-shadow: 0 6px 18px rgba(0,0,0,0.18);
  }

  /* Contact side */
  .card--contact { display: flex; background: var(--card-dark); }
  .brand-panel {
    width: 44%;
    background: linear-gradient(160deg, var(--brand-blue) 0%, var(--brand-blue-deep) 100%);
    display: flex;
    align-items: center;
    justify-content: center;
    padding: 0 22px;
  }
  .brand-panel .company-name {
    color: var(--text-light);
    font-weight: 300;
    font-size: 17px;
    line-height: 1.3;
    text-align: center;
  }
  .details-panel {
    flex: 1;
    padding: 30px 26px 0 30px;
    color: var(--text-light);
  }
  .person-name { font-weight: 700; font-size: 23px; letter-spacing: 0.2px; }
  .person-role { font-weight: 700; font-size: 9px; margin-top: 2px; }
  .job-list { list-style: none; margin-top: 6px; }
  .job-list li {
    color: var(--brand-blue);
    font-size: 11.5px;
    line-height: 1.3;
    font-weight: 400;
  }
  .contact-list { list-style: none; margin-top: 20px; }
  .contact-list li {
    display: flex;
    align-items: center;
    gap: 10px;
    font-size: 11.5px;
    color: var(--text-light);
    height: 22px;
  }
  .contact-list svg { width: 15px; height: 15px; flex: none; }

  /* Brand side */
  .card--brand {
    background: radial-gradient(ellipse at 40% 30%, var(--card-dark-2) 0%, var(--card-dark) 70%);
    display: flex;
    align-items: center;
    justify-content: center;
  }
  .card--brand .company-name {
    color: var(--brand-blue);
    font-weight: 300;
    font-size: 26px;
    text-align: center;
    line-height: 1.35;
    letter-spacing: 0.3px;
  }
</style>
</head>
<body>

  <section class="card card--contact" aria-label="Contact side">
    <div class="brand-panel">
      <p class="company-name">Velbridge Consulting Services</p>
    </div>
    <div class="details-panel">
      <h1 class="person-name">Your Name Here</h1>
      <p class="person-role">CEO</p>
      <ul class="job-list">
        <li>ICO Advisor</li>
        <li>World Champion Gamer</li>
        <li>Esports Award Winner</li>
        <li>Varlomark Expert</li>
      </ul>
      <ul class="contact-list">
        <li>
          <svg viewBox="0 0 16 16" aria-hidden="true"><circle cx="8" cy="8" r="7" fill="var(--icon-grey)"/></svg>
          @yourusername
        </li>
        <li>
          <svg viewBox="0 0 16 16" aria-hidden="true"><path d="M3.5 1.5l2.5 0 1 3.5-1.6 1.2a8 8 0 0 0 4.4 4.4l1.2-1.6 3.5 1v2.5c0 .8-.7 1.5-1.5 1.5C7 14 2 9 2 3c0-.8.7-1.5 1.5-1.5z" fill="none" stroke="var(--icon-grey)" stroke-width="1.3"/></svg>
          (00) 0000 0000
        </li>
        <li>
          <svg viewBox="0 0 16 16" aria-hidden="true"><rect x="4" y="1" width="8" height="14" rx="1.5" fill="none" stroke="var(--icon-grey)" stroke-width="1.3"/><circle cx="8" cy="12.5" r="0.9" fill="var(--icon-grey)"/></svg>
          (00) 0000 0000
        </li>
        <li>
          <svg viewBox="0 0 16 16" aria-hidden="true"><rect x="1.5" y="3.5" width="13" height="9" rx="1" fill="none" stroke="var(--icon-grey)" stroke-width="1.3"/><path d="M1.5 4l6.5 5 6.5-5" fill="none" stroke="var(--icon-grey)" stroke-width="1.3"/></svg>
          yourbusiness@velbridge-mail.com
        </li>
        <li>
          <svg viewBox="0 0 16 16" aria-hidden="true"><circle cx="8" cy="8" r="6.5" fill="none" stroke="var(--icon-grey)" stroke-width="1.3"/><path d="M1.5 8h13M8 1.5c2.2 2 2.2 11 0 13M8 1.5c-2.2 2-2.2 11 0 13" fill="none" stroke="var(--icon-grey)" stroke-width="1"/></svg>
          www.velbridge.com
        </li>
      </ul>
    </div>
  </section>

  <section class="card card--brand" aria-label="Brand side">
    <p class="company-name">Velbridge<br>Consulting Services</p>
  </section>

</body>
</html>
```